Wired Earphone Creative Packaging Design

We would like a creative window box style packaging design for our wired earphone

Size: 6” x 3.5” x 1.5” (enclosed die-cut drawing)
Material: E Flute Paper box
Type: Window Box style
Design features we prefer: friendly, playful, creative, trendy, unique, High tech.
Competitors: Enclosed
Requirement:AI file is preferred

Enclosed are product pictures, marketing materials and competitor designs for your reference.

Any further questions, please feel free to ask.
Updates

So designers get more time to design

Target Market(s)

13-40 Year Olds

Industry/Entity Type

Audio

Colors

Designer to choose colors to be used in the design.

Requirements
Must have
• Window, selling point, creative

```html
<!DOCTYPE html>
<html lang="en">
<head>
<meta charset="utf-8">
<title>VK-7 Earphone Window Box Dieline</title>
<link rel="stylesheet" href="https://fonts.googleapis.com/css2?family=Teko:wght@600&family=Montserrat:wght@800&family=Roboto:wght@400;500&display=swap">
<style>
:root{
  --bg:#ececec;
  --yellow:#f3c623;
  --charcoal:#404040;
  --flap:#ffffff;
  --side:#e5e5e5;
  --line:#cfcfcf;
  --ink:#3a3a3a;
  --window:#a9a9a9;
}
*{margin:0;padding:0;box-sizing:border-box}
html,body{width:1200px;height:1000px;overflow:hidden;background:var(--bg)}
.canvas{position:relative;width:1200px;height:1000px}
.dieline{position:absolute;inset:0}
.abs{position:absolute}
.title-block{left:562px;top:279px;width:286px;text-align:center;font-family:"Montserrat",sans-serif;font-weight:800;font-size:15.5px;line-height:24px;color:var(--charcoal);letter-spacing:.2px}
.vertical-tagline{font-family:"Roboto",sans-serif;font-size:18px;color:#fff;white-space:nowrap;top:510px;transform-origin:center}
.vertical-tagline em{font-style:normal;color:var(--yellow)}
.tagline-left{left:494px;transform:translate(-50%,-50%) rotate(90deg)}
.tagline-right{left:909px;transform:translate(-50%,-50%) rotate(-90deg)}
.product-window{left:530px;top:331px;width:352px;height:358px;border-radius:14px;background:radial-gradient(ellipse at center,#c4c4c4,var(--window));overflow:hidden}
.name-band{left:530px;top:459px;width:352px;height:102px;background:var(--yellow);display:flex;align-items:center;justify-content:center}
.name-band .model{font-family:"Teko",sans-serif;font-weight:600;font-size:112px;line-height:1;color:var(--charcoal);margin-top:16px}
.band-mark{font-family:"Teko",sans-serif;font-weight:600;font-size:38px;color:var(--charcoal);top:510px;line-height:1}
.band-mark-left{left:552px;transform:translate(-50%,-50%) rotate(90deg)}
.band-mark-right{left:858px;transform:translate(-50%,-50%) rotate(-90deg)}
.features{left:577px;top:700px;font-family:"Montserrat",sans-serif;font-weight:800;font-size:8.5px;line-height:10.5px;color:var(--charcoal);display:flex;gap:12px;letter-spacing:.4px}
.features ul{list-style:none}
.features li::before{content:"• "}
.side-panel{left:150px;top:268px;width:284px;height:484px;background:var(--side);font-family:"Roboto",sans-serif;color:var(--ink)}
.side-panel .subtitle{position:absolute;left:14px;top:17px;font-size:13px}
.side-panel .model{position:absolute;left:10px;top:42px;font-family:"Teko",sans-serif;font-weight:600;font-size:92px;line-height:1;color:var(--charcoal)}
.side-panel .product-shot{position:absolute;left:164px;top:36px;width:120px;height:86px;border-radius:40px 10px 40px 20px;background:linear-gradient(135deg,#f4f4f4,#e8d27a 60%,#cfcfcf)}
.spec{position:absolute;left:16px;font-size:13px;line-height:23px}
.spec ul{list-style:none;padding-left:8px}
.spec li::before{content:"•";margin-right:10px}
.spec-contents{top:139px}
.spec-specs{top:242px}
</style>
</head>
<body>
<div class="canvas">
  <svg class="dieline" width="1200" height="1000" viewBox="0 0 1200 1000" aria-hidden="true">
    <!-- top flaps -->
    <rect x="150" y="150" width="283" height="118" fill="var(--flap)" stroke="var(--line)"/>
    <rect x="207" y="200" width="169" height="12" rx="6" fill="#dcdcdc"/>
    <path d="M443 268V160q0-8 8-8h28q8 0 8 8v40h8v-40q0-8 8-8h42q8 0 8 8v108z" fill="var(--flap)" stroke="var(--line)"/>
    <path d="M858 268V160q0-8 8-8h42q8 0 8 8v40h8v-40q0-8 8-8h28q8 0 8 8v108z" fill="var(--flap)" stroke="var(--line)"/>
    <path d="M562 268V145h286v123z" fill="var(--yellow)"/>
    <path d="M610 145V115q0-22 22-22h144q22 0 22 22v30l-93 92z" fill="var(--charcoal)"/>
    <rect x="620" y="199" width="170" height="13" rx="6.5" fill="#fff"/>
    <!-- front panel -->
    <rect x="434" y="268" width="536" height="484" fill="var(--charcoal)"/>
    <rect x="462" y="268" width="480" height="484" fill="var(--yellow)"/>
    <polygon points="470,268 540,332 540,690 470,752" fill="var(--charcoal)"/>
    <polygon points="934,268 870,332 870,690 934,752" fill="var(--charcoal)"/>
    <!-- glue flap -->
    <polygon points="970,268 1035,278 1035,742 970,752" fill="var(--flap)" stroke="var(--line)"/>
    <!-- bottom flaps -->
    <path d="M437 752h116v116h-60v-30h-8v30h-40q-8 0-8-8z" fill="var(--flap)" stroke="var(--line)"/>
    <path d="M858 752h102v108q0 8-8 8h-40v-30h-8v30h-46z" fill="var(--flap)" stroke="var(--line)"/>
    <path d="M562 752h286v150H562z" fill="var(--yellow)"/>
    <path d="M563 900l142-140 143 140v0q0 26-26 26H589q-26 0-26-26z" fill="var(--charcoal)"/>
  </svg>

  <div class="abs title-block">CUSTOMIZABLE<br>STEREO IN- EAR EARPHONES</div>

  <div class="abs vertical-tagline tagline-left">Customizable <em>Stereo</em> In-Ear Earphones</div>
  <div class="abs vertical-tagline tagline-right">Customizable <em>Stereo</em> In-Ear Earphones</div>

  <div class="abs product-window" role="img" aria-label="Window showing the white and orange earbuds, in-line mic remote and yellow swappable caps"></div>
  <div class="abs name-band"><span class="model">VK-7</span></div>
  <div class="abs band-mark band-mark-left">VK-7</div>
  <div class="abs band-mark band-mark-right">VK-7</div>

  <div class="abs features">
    <ul>
      <li style="list-style:none">FEATURES:</li>
      <li>CUSTOMIZABLE EARBUDS</li>
      <li>IN LINE MIC</li>
      <li>SILICONE GEL EAR TIPS</li>
    </ul>
    <ul style="margin-top:10.5px">
      <li>3.5MM JACK</li>
      <li>ERGONOMIC DESIGN</li>
    </ul>
  </div>

  <section class="abs side-panel">
    <p class="subtitle">Customizable Stereo In- Ear Earphones</p>
    <p class="model">VK-7</p>
    <div class="product-shot" role="img" aria-label="Earbuds with assorted interchangeable caps"></div>
    <div class="spec spec-contents">
      <p>Contents :</p>
      <ul>
        <li>2 Pairs of Switchable Caps</li>
        <li>3 Pairs of Silicone Ear tips</li>
        <li>User Manual</li>
      </ul>
    </div>
    <div class="spec spec-specs">
      <p>Specification:</p>
      <ul>
        <li>Frequency Response: 20-20KHz</li>
        <li>Sensitivity: 105±3dB</li>
        <li>THD: &lt;3%</li>
        <li>Cord Length: 3.6ft</li>
      </ul>
    </div>
  </section>
</div>
</body>
</html>
```